依頼詳細
ロゴのデザインはきまっております。
その為、ロゴのイメージに添って名刺のデザインも考慮して頂けると幸いです。
テーマカラーは青(最も好かれる色だそうでこれにしました)
ロゴのイメージを解説すると、アルファベットのTをモチーフにしております。
事務所名が みなせ社会保険労務士事務所なので、その頭文字を取りました。

右肩上がりに成長するとともに、一つの星(他者貢献という導きの星、ヴェルナー心理学から影響を受けました)を指針として事務所を経営していくことを目指しております。

名刺のイメージですが、基本的には信頼感、高級感が有りながら、遊び心もあると名刺を受け取って頂いた際に話の種になるかもしれません。
ちなみに参考までに私のサイトのURLはwww.nobiru-sr.tvです。 テーマカラーはオレンジとみどりですが、これは青のサイトが多い故にわざと青色は外しました。

重視するポイントは、名刺をもらうとちょっと遊び心があると素敵だと思います。
従業員は2名おりまして、いずれも女性なので、それも考慮していただくといいかもしれません。

デザインに詳しくないので、あまり具体的なイメージが浮かばず申し訳ないのですが、ロゴとホームページからイメージが湧くことがあれば幸いです

海外っぽい名刺なんかかっこいいですね(大味)

フォントはヒラギノなんか好きです。業者に印刷は頼みますのでそこは提案として気にしません。

趣味は読書で、月に10冊は読んでます
好きなものは可愛いものが好きです(モフタロウ、ピコすけ、ロロ)
ネコ派です
この情報は一切関係なくて構いません。あくまでそういう人間だということで
33歳の男性です。従業員は33歳女性、56歳女性です
選定はする予定です。
記載項目
表:キャッチフレーズ、事務所名、役職、氏名、電話番号、ファックス番号、メールアドレス、ホームページURL、
裏:業務内容、取得資格、最終学歴
希望イメージ
シンプル 複雑
単色 カラフル
暗い 明るい
日常 高級
遊び心 厳粛
未来的 伝統的
女性的 男性的
希望する色
青系
納品ファイル
• 高解像度JPG (.jpg)
• イラストレーター形式 (.ai)
• フォトショップ形式 (.psd)
• PNG形式 (.png)
補足説明
納品ファイルは、名刺印刷業者に渡すのでイラストレーターがいいかと思いますが、おまかせします。

非常に沢山のご提案があり最後の最後まで悩み抜きました。
結果として、どうしても分けられない2つを手放せなくなり2案当選になりました。
ネコバージョンとスタイリッシュバージョンの2パターンを使い分けていきたいと思います。

ポイントは、ネコバージョンは正直予想してませんでした。デザイン会社ではなかなか出会えないであろう遊び心に心打たれてしまいました。

もう一つのほうは右肩上がりというところを意識していただいたところです。
ロゴだけでなく、名刺そのものが右肩上がりであり、Tに見えるデザインが気に入りました。

本当にたくさんのご提案を有難うございました。
依頼当初はここまで集まるとは思ってもみず、クリエルの皆様の素晴らしさと心意気に感動しました。
ロゴは別会社で作ったのですが、ココで頼めばもっと。。。と思わなくもありません。
私のために時間をさいて考えてくださって感謝の言葉もございません。
参加報酬と言うかたちで恐縮ではありますが、4名選ばさせていただきました。
依頼途中に横バージョンも見たいなどとわがままを申し出たことお許し下さい。

ほんとうに有難うございました。

```html
<!DOCTYPE html>
<html lang="ja">
<head>
<meta charset="UTF-8">
<title>みなせ社会保険労務士事務所 名刺</title>
<link href="https://fonts.googleapis.com/css2?family=Noto+Sans+JP:wght@400;500;700&family=Noto+Serif+JP:wght@500&display=swap" rel="stylesheet">
<style>
  :root{
    --bg:#eceef1;
    --card:#ffffff;
    --navy:#12397f;
    --blue:#1f6cc4;
    --blue-mid:#5c97d8;
    --blue-light:#c6daf2;
    --blue-faint:#eef3fa;
    --ink:#2b2f36;
    --muted:#6b7380;
    --line:#b9cbe4;
  }
  *{margin:0;padding:0;box-sizing:border-box}
  html,body{width:812px;height:1200px;overflow:hidden;background:var(--bg)}
  body{font-family:"Noto Sans JP",sans-serif;color:var(--ink);position:relative}
  .card{position:absolute;left:24px;width:764px;height:462px;background:var(--card);overflow:hidden;box-shadow:0 2px 8px rgba(0,0,0,.12)}
  .card--front{top:110px}
  .card--back{top:628px}
  .accent-area{position:absolute;left:410px;top:0;width:354px;height:250px;background:linear-gradient(200deg,var(--navy) 0%,var(--blue) 40%,var(--blue-mid) 70%,var(--blue-light) 100%)}
  .catch{position:absolute;left:44px;top:44px;font-size:30px;font-weight:500;color:var(--blue);letter-spacing:.04em}
  .office{position:absolute;left:44px;top:128px;font-size:21px;font-weight:500;color:var(--blue)}
  .address{position:absolute;left:44px;top:166px;font-size:14px;color:var(--blue);line-height:21px}
  .contacts{position:absolute;left:44px;top:210px;display:flex;gap:26px;font-size:14px;color:var(--blue)}
  .contact{display:flex;align-items:center;gap:6px}
  .icon{width:16px;height:14px;fill:var(--blue)}
  .mark{position:absolute;display:flex;flex-direction:column;align-items:center;gap:10px}
  .mark__dot{border-radius:50%;background:var(--navy)}
  .mark__name{font-weight:700;color:var(--navy);letter-spacing:.08em}
  .mark--front{left:40px;top:292px}
  .mark--front .mark__dot{width:96px;height:96px}
  .mark--front .mark__name{font-size:26px}
  .url{position:absolute;left:236px;top:424px;font-size:17px;color:var(--blue);letter-spacing:.03em}
  .person{position:absolute;left:515px;top:316px}
  .person__role{font-size:14px;color:var(--ink)}
  .person__name{font-family:"Noto Serif JP",serif;font-size:38px;font-weight:500;letter-spacing:.12em;line-height:1.2;color:var(--ink)}
  .person__roman{font-family:"Noto Serif JP",serif;font-size:12px;color:var(--muted)}
  .person__line{display:flex;align-items:center;gap:6px;font-size:13px;color:var(--blue);margin-top:6px}
  .ghost{position:absolute;left:250px;top:-90px;width:320px;height:320px;border-radius:50%;background:var(--blue-faint)}
  .sections{position:absolute;left:160px;top:92px}
  .section{display:flex;position:relative;padding-left:20px;margin-bottom:28px}
  .section::before{content:"";position:absolute;left:0;top:2px;width:5px;height:22px;background:var(--blue)}
  .section--rail::after{content:"";position:absolute;left:1px;top:24px;bottom:-28px;width:3px;background:var(--line)}
  .section__label{width:150px;font-size:16px;font-weight:500;color:var(--blue);letter-spacing:.1em;border-bottom:1px solid var(--line);height:26px}
  .section__items{font-size:14px;line-height:22px;color:var(--ink)}
  .mark--back{left:598px;top:262px}
  .mark--back .mark__dot{width:86px;height:86px}
  .mark--back .mark__name{font-size:23px}
</style>
</head>
<body>
  <section class="card card--front">
    <div class="accent-area" role="img" aria-label="右肩上がりの青い曲線装飾"></div>
    <div class="catch">キャッチフレーズ</div>
    <div class="office">みなせ社会保険労務士事務所</div>
    <div class="address">〒000-0000<br>住所住所住所住所住所住所住所</div>
    <div class="contacts">
      <span class="contact"><svg class="icon" viewBox="0 0 16 14"><path d="M1 4 C1 1 4 0 8 0 C12 0 15 1 15 4 L11 5 L10 3 L6 3 L5 5 Z M3 6 L13 6 L15 13 L1 13 Z"/></svg>00-0000-0000</span>
      <span class="contact"><svg class="icon" viewBox="0 0 16 14"><path d="M4 0 L12 0 L12 4 L4 4 Z M0 5 L16 5 L16 13 L0 13 Z"/></svg>00-0000-0000</span>
    </div>
    <div class="mark mark--front"><span class="mark__dot"></span><span class="mark__name">MINASE</span></div>
    <div class="url">www.xxxxxxxxxx.co.jp</div>
    <div class="person">
      <div class="person__role">代表</div>
      <div class="person__name">山田 太郎</div>
      <div class="person__roman">Taro Yamada</div>
      <div class="person__line"><svg class="icon" viewBox="0 0 16 14"><path d="M5 0 L11 0 L11 14 L5 14 Z"/></svg>000-0000-0000</div>
      <div class="person__line"><svg class="icon" viewBox="0 0 16 14"><path d="M0 2 L16 2 L16 12 L0 12 Z"/></svg>xxxxx@xxxxx.com</div>
    </div>
  </section>

  <section class="card card--back">
    <div class="ghost"></div>
    <div class="sections">
      <div class="section section--rail">
        <div class="section__label">業務内容</div>
        <div class="section__items">人事・労務管理業務<br>就業規則の作成業務<br>手続代行業務<br>助成金の申請業務</div>
      </div>
      <div class="section">
        <div class="section__label">取得資格</div>
        <div class="section__items">行政書士<br>宅地建物取引士<br>2級FP技能士<br>ビジネス著作権上級<br>社会保険労務士</div>
      </div>
      <div class="section">
        <div class="section__label">最終学歴</div>
        <div class="section__items">北稜大学法学部卒業</div>
      </div>
    </div>
    <div class="mark mark--back"><span class="mark__dot"></span><span class="mark__name">MINASE</span></div>
  </section>
</body>
</html>
```